Website Redesign for Technology Focused Investment Bank

We need a website redesign for a technology and digital media focused investment banking firm. Think modern and forward thinking yet stable and smart. We provide mergers and acquisitions advisory services to our clients. Our target market are CEO's and CFO's (senior executives) that run and operate technology firms.

Kestrel Bay Advisors - www.kestrelbayadvisors.example

We are headquartered in Los Angeles, CA. Please do NOT use the Brindle Arch for anything.

We have the content and can update the photos as well.

We are looking for a "template" website we can update and edit with ease.

A competitive firm's website is: www.dunmoregrey.example Not sure I like it but I want it to look way better then this one.

Looking for a more modern version. Not too stuffy and conservative, please. Elegant, smart, updated and progressive/modern.
Updates

Color preferences:  Blue's including matching logo color. Grey's. You can add other colors if it flows well and looks clean and nice.

Menu:  Drop Down

Open to platform...please use one that most people can use, is reasonably priced if I need to buy it, and easy to update monthly and sometimes weekly.

Please use this website as a good example of what we are looking for (or similar version of it): www.plorvex.example

Thanks!
Tobias R.

We are reviewing all submissions and will select one this week. Thank you everyone for your outstanding and creative designs you have sent us. We really appreciate it.

Thanks for everyone's hard work and creative input into our website design. We really appreciate it!

Target Market(s)

CEO's and CFO's, Entrepreneurs and Board Members of Technology Companies.

Industry/Entity Type

Investment

Font styles to use
Sans Serif

Colors
33a6d7
0492cd
0555a3
3176b5
85abd2
333333
5c5c5c
757575

Requirements
Must have
• Links to social media including Twitter, LinkedIn, Google+, Facebook, etc.

Must try to match logo color
Should not have
• No conservative, old looking colors or background. For example, no green marble look.

```html
<!DOCTYPE html>
<html lang="en">
<head>
<meta charset="utf-8">
<title>Kestrel Bay Advisors</title>
<link href="https://fonts.googleapis.com/css2?family=Arimo:wght@400;700&display=swap" rel="stylesheet">
<style>
:root{
  --blue-bright:#33a6d7;
  --blue-mid:#0492cd;
  --blue-deep:#0555a3;
  --blue-brand:#3176b5;
  --blue-soft:#85abd2;
  --ink:#333333;
  --grey:#5c5c5c;
  --grey-light:#757575;
  --footer:#1e1b1b;
  --white:#ffffff;
}
*{box-sizing:border-box;margin:0;padding:0}
html,body{width:1199px;height:1200px;overflow:hidden}
body{font-family:"Arimo",Arial,sans-serif;color:var(--grey);background:var(--white);position:relative}
a{color:inherit;text-decoration:none}

.site-header{position:absolute;top:0;left:0;width:1199px;height:78px;background:var(--white)}
.brand{position:absolute;left:292px;top:20px;display:flex;align-items:center;gap:10px}
.brand-mark{width:36px;height:36px;border-radius:50%;background:var(--blue-brand)}
.brand-name{font-size:19px;color:var(--blue-deep);line-height:1.1}
.main-nav{position:absolute;left:497px;top:48px;display:flex}
.main-nav a{font-size:8.5px;font-weight:700;color:var(--grey-light);letter-spacing:.4px;padding:0 22px;border-left:1px solid #ddd}
.main-nav a:first-child{padding-left:0;border-left:none}

.hero{position:absolute;top:78px;left:0;width:1199px;height:446px;overflow:hidden}
.hero-photo{position:absolute;inset:0;background:linear-gradient(180deg,#8fa8bf 0%,#b9cbd9 35%,#c8c4bc 58%,#7a5a4a 75%,#4a3129 100%)}
.hero-arrow{position:absolute;top:189px;width:52px;height:52px;border-radius:50%;background:rgba(200,200,200,.8);color:var(--white);font-size:22px;display:flex;align-items:center;justify-content:center}
.hero-arrow.prev{left:-26px;justify-content:flex-end;padding-right:10px}
.hero-arrow.next{right:-26px;justify-content:flex-start;padding-left:10px}
.dropdown{position:absolute;left:289px;top:0;width:165px;height:325px;background:var(--white);padding:12px 21px}
.dropdown a{display:block;font-size:8.5px;color:var(--grey);height:26.2px;line-height:26px;border-bottom:1px solid #e6e6e6;width:98px}
.dropdown a.active{color:var(--blue-deep);font-weight:700}
.dropdown a:last-child{border-bottom:none}
.dropdown-toggle{position:absolute;left:339px;top:300px;width:50px;height:50px;border-radius:50%;background:var(--white);display:flex;align-items:center;justify-content:center;color:var(--blue-deep);font-weight:700;font-size:16px;padding-top:6px}
.hero-caption{position:absolute;left:640px;top:240px;width:303px;height:84px;background:rgba(255,255,255,.72);text-align:right;padding:22px 28px 0 0}
.hero-caption .kicker{font-size:17px;color:var(--ink)}
.hero-caption .title{font-size:18px;font-weight:700;color:var(--blue-deep);margin-top:6px}

.follow-band{position:absolute;top:524px;left:0;width:1199px;height:93px;background:var(--blue-bright);color:var(--white)}
.band-intro{position:absolute;left:289px;top:24px;width:350px;font-size:8.5px;line-height:14px}
.band-intro .more{display:inline-block;margin-top:12px;font-weight:700;text-decoration:underline}
.band-divider{position:absolute;left:641px;top:22px;width:1px;height:50px;background:rgba(255,255,255,.3)}
.follow-label{position:absolute;left:701px;top:36px;font-size:17px}
.social{position:absolute;left:822px;top:34px;display:flex;gap:6px}
.social span{width:26px;height:26px;background:var(--ink);display:block}

.content{position:absolute;top:617px;left:0;width:1199px;height:431px;background:linear-gradient(110deg,#f4f5f8 0%,#e6e9ee 40%,#f2f3f6 60%,#e4e7ec 100%)}
.col{position:absolute;top:48px;font-size:8.5px;line-height:13.2px;color:var(--grey-light)}
.col h2{font-size:14px;font-weight:400;color:var(--blue-brand);margin-bottom:22px}
.col p{margin-bottom:13px}
.col-why{left:289px;width:185px}
.col-process{left:506px;width:245px}
.process-photo{width:245px;height:107px;background:linear-gradient(135deg,#0a3f8c,#3a7fd0 50%,#cfe0f3);margin-bottom:16px}
.col-tweets{left:779px;width:178px;font-size:6.5px;line-height:13px}
.col-tweets h3{font-size:10px;font-weight:400;color:var(--grey);margin:6px 0 22px}
.tweet{margin-bottom:44px}
.tweet .link{color:var(--blue-mid)}
.tweet .time{font-size:5.5px;color:#999}

.site-footer{position:absolute;top:1048px;left:0;width:1199px;height:152px;background:var(--footer);color:#cfcfcf}
.subscribe{position:absolute;left:290px;top:34px;width:230px}
.subscribe h4,.site-links h4{font-size:10px;font-weight:400;color:var(--white);letter-spacing:.3px}
.subscribe .hint{font-size:6px;color:#8a8a8a;margin:12px 0 6px}
.subscribe-form{width:218px;height:28px;background:var(--blue-mid);border-radius:4px;display:flex;align-items:center;padding:0 6px;gap:6px;font-size:7px;color:var(--white);white-space:nowrap}
.subscribe-form .field{width:95px;height:17px;background:var(--white);border-radius:4px;flex:none}
.subscribe-form .btn{height:17px;padding:0 10px;border-radius:8px;background:var(--ink);line-height:17px;font-size:6.5px;flex:none}
.rss{display:flex;align-items:center;gap:10px;font-size:6.5px;color:#8a8a8a;margin-top:9px}
.rss .dot{width:10px;height:10px;background:#f08a24;border-radius:2px}
.rss a{color:var(--blue-bright);text-decoration:underline}
.site-links{position:absolute;left:589px;top:34px}
.site-links ul{list-style:none;margin-top:10px}
.site-links li{font-size:6.5px;line-height:15.5px;color:#bdbdbd}
.footer-brand{position:absolute;left:787px;top:76px;display:flex;align-items:center;gap:8px}
.footer-brand .brand-mark{width:36px;height:36px;background:#5e5e5e}
.footer-brand .brand-name{font-size:16px;color:#6f6f6f}
.copyright{position:absolute;left:795px;top:120px;font-size:5.5px;color:#555}
</style>
</head>
<body>
<header class="site-header">
  <a class="brand" href="#"><span class="brand-mark"></span><span class="brand-name">Kestrel Bay<br>Advisors</span></a>
  <nav class="main-nav"><a href="#">ABOUT US</a><a href="#">SERVICES</a><a href="#">CONTACT US</a></nav>
</header>

<section class="hero">
  <div class="hero-photo" role="img" aria-label="Photo of a modern glass-roofed boardroom with a long table and leather chairs"></div>
  <a class="hero-arrow prev" href="#">&#10094;</a>
  <a class="hero-arrow next" href="#">&#10095;</a>
  <div class="dropdown-toggle">&ndash;</div>
  <nav class="dropdown">
    <a class="active" href="#">Home</a><a href="#">About Us</a><a href="#">Services</a><a href="#">Transactions</a><a href="#">Research</a><a href="#">Private Equity</a><a href="#">Recommendations</a><a href="#">About the Founder</a><a href="#">Careers</a><a href="#">News+Blog</a><a href="#">Contact Us</a>
  </nav>
  <div class="hero-caption"><div class="kicker">Technology and Digital Media</div><div class="title">Investment Banking</div></div>
</section>

<section class="follow-band">
  <div class="band-intro">Lorem ipsum dolor sit amet, consectetur adipisicing elit, sed do eiusmod tempor incididunt ut labore et dolore magna aliqua. Ut enim ad minim veniam, quis nostrud exercitation ullamco<br><a class="more" href="#">+ LEARN MORE</a></div>
  <div class="band-divider"></div>
  <div class="follow-label">FOLLOW US</div>
  <div class="social"><span aria-label="Social profile link"></span><span aria-label="Social profile link"></span><span aria-label="Social profile link"></span><span aria-label="Social profile link"></span></div>
</section>

<main class="content">
  <div class="col col-why">
    <h2>Why Us?</h2>
    <p>We are an independent investment bank and M&amp;A advisory firm focused exclusively on the global Technology and Digital Media sectors. Specifically, we execute mergers and acquisitions for the Software, IT Services, Internet and Digital Media industry sectors.</p>
    <p>Our professionals have completed over $20 billion in transactions to date and have experience in investment banking, private equity and capital markets from leading firms. We are experts in complex M&amp;A transactions of most shapes and sizes and have deep industry expertise.<br>We advise companies, entrepreneurs, majority shareholders and leading institutions on complex strategic</p>
  </div>
  <div class="col col-process">
    <h2>M&amp;A Process</h2>
    <div class="process-photo" role="img" aria-label="Close-up photo of a printed financial report in blue tones"></div>
    <p>Our M&amp;A process helps clients achieve maximum success and increased shareholder value.</p>
    <p>We operate without conflicts of interests unlike the larger investment banking firms and do not trade in securities or provide investment research. We are independent and specialize in offering focused advice on technology and digital media industry specific mergers &amp; acquisitions.</p>
    <p>We operate with a global view and advise companies strictly within our industry expertise.</p>
    <p>We do not accept customer deposits nor do we provide investment advice to individuals or institutions. Our business is strictly mergers &amp; acquisitions.</p>
  </div>
  <div class="col col-tweets">
    <h3>Tweets by @TechDealDesk</h3>
    <div class="tweet"><div class="link">http://abc/dealnotes.example/</div>Lorem ipsum dolor sit amet, consectetur adipisicing elit, sed do eiusmod tempor incididunt ut labore et dolore magna aliqua. Ut enim ad minim veniam, quis nostrud<div class="time">2 min ago</div></div>
    <div class="tweet"><div class="link">http://abc/dealnotes.example/</div>Lorem ipsum dolor sit amet, consectetur adipisicing elit, sed do eiusmod tempor incididunt ut labore et dolore magna aliqua. Ut enim ad minim veniam, quis nostrud<div class="time">2 min ago</div></div>
  </div>
</main>

<footer class="site-footer">
  <div class="subscribe">
    <h4>SUBSCRIBE TO OUR <b>M&amp;A</b> UPDATES</h4>
    <p class="hint">Enter your e-mail address below to receive regular updates</p>
    <div class="subscribe-form"><span>Email Address</span><span class="field"></span><span class="btn">SUBSCRIBE</span></div>
    <div class="rss"><span class="dot"></span><span>Subscribe to the <a href="#">Company Name articles RSS feed</a></span></div>
  </div>
  <div class="site-links">
    <h4>SITE LINKS</h4>
    <ul><li>Transactions</li><li>Research</li><li>Private Equity</li><li>Careers</li><li>Blog</li><li>Contact Us</li></ul>
  </div>
  <div class="footer-brand"><span class="brand-mark"></span><span class="brand-name">Kestrel Bay<br>Advisors</span></div>
  <div class="copyright">Copyright Company Name All Right Reserved 2014</div>
</footer>
</body>
</html>
```